Marrowfield Contracting Business Cards

Front of card:

Full Logo
Name
Address
Office Phone
Cell Phone
Email
Website

Back:
Logo Mark in background
List and markets and services performed

```html
<!DOCTYPE html>
<html lang="en">
<head>
<meta charset="utf-8">
<title>Marrowfield Contracting – Business Cards</title>
<link rel="stylesheet" href="https://fonts.googleapis.com/css2?family=Ubuntu:wght@400;700&family=Open+Sans:wght@400;600;700&display=swap">
<style>
  :root{
    --stage:#14101f;
    --brand-red:#d41317;
    --brand-grey:#606060;
    --card-white:#f5f5f5;
    --ink:#3a3a3a;
    --white:#ffffff;
  }
  *{box-sizing:border-box;margin:0;padding:0}
  html,body{width:1200px;height:994px;overflow:hidden}
  body{background:var(--stage);font-family:"Open Sans",sans-serif;position:relative}

  .card{position:absolute;width:700px;height:400px;overflow:hidden;border-radius:4px;box-shadow:0 18px 40px rgba(0,0,0,.5)}
  .card--front{left:100px;top:57px;background:var(--card-white)}
  .card--back{left:400px;top:537px;background:var(--brand-red)}

  /* front */
  .front-shapes{position:absolute;inset:0}
  .brand-name{position:absolute;font-family:"Ubuntu",sans-serif;font-weight:700;text-transform:uppercase;line-height:1.05;display:flex;align-items:center;gap:10px}
  .brand-name__dot{border-radius:50%;flex:none}
  .front-brand{left:36px;top:46px;color:var(--brand-red);font-size:24px}
  .front-brand .brand-name__dot{width:34px;height:34px;background:var(--brand-red)}
  .holder-name{position:absolute;left:36px;top:160px;font-family:"Ubuntu",sans-serif;font-weight:700;font-size:30px;color:var(--white)}
  .holder-email{position:absolute;left:36px;top:214px;font-size:16px;color:var(--white);display:flex;align-items:center;gap:8px}
  .contact-list{position:absolute;left:50px;top:262px;list-style:none;font-size:16px;color:var(--ink)}
  .contact-list li{display:flex;align-items:center;gap:10px;height:30px}
  .contact-list svg{flex:none}
  .divider{position:absolute;left:470px;top:250px;width:1px;height:90px;background:#c9c9c9}
  .address{position:absolute;left:490px;top:160px;font-size:17px;line-height:1.2;color:var(--ink);display:flex;gap:6px}
  .address__company{color:var(--brand-red)}

  /* back */
  .mark-decoration{position:absolute;left:420px;top:40px;width:320px;height:320px;border-radius:50%;background:rgba(255,255,255,.16)}
  .back-brand{left:40px;top:40px;color:var(--white);font-size:26px}
  .back-brand .brand-name__dot{width:40px;height:40px;border:4px solid var(--white)}
  .rule{position:absolute;height:1.5px;background:var(--white)}
  .rule--top{left:40px;top:112px;width:250px}
  .services-title{position:absolute;left:40px;top:126px;font-family:"Ubuntu",sans-serif;font-weight:700;font-size:26px;color:var(--white)}
  .rule--mid{left:40px;top:172px;width:300px}
  .rule-dot{position:absolute;left:338px;top:168px;width:9px;height:9px;border-radius:50%;background:var(--white)}
  .services-list{position:absolute;left:56px;top:190px;list-style:none;font-size:17px;color:var(--white)}
  .services-list li{display:flex;align-items:center;gap:8px;height:30px}
  .back-web{position:absolute;left:56px;top:330px;font-size:16px;color:var(--white);display:flex;align-items:center;gap:8px}
</style>
</head>
<body>

<section class="card card--front" aria-label="Business card front">
  <svg class="front-shapes" viewBox="0 0 700 400" width="700" height="400" aria-hidden="true">
    <path d="M0 150 H400 C450 150 470 80 530 80 H700 V135 H540 C490 135 470 205 410 205 H0 Z" fill="var(--brand-red)"/>
    <path d="M0 205 H410 C470 205 490 135 540 135 H560 C510 135 490 245 420 245 H0 Z" fill="var(--brand-grey)"/>
    <circle cx="610" cy="100" r="52" fill="var(--card-white)"/>
    <circle cx="610" cy="100" r="42" fill="var(--brand-red)"/>
  </svg>

  <div class="brand-name front-brand">
    <span class="brand-name__dot"></span>
    <span>Marrowfield<br>Contracting LLC</span>
  </div>

  <h1 class="holder-name">Daniel Hartley</h1>
  <p class="holder-email">
    <svg width="16" height="12" viewBox="0 0 16 12" aria-hidden="true"><rect x="0.5" y="0.5" width="15" height="11" fill="none" stroke="#fff"/><path d="M0.5 0.5 L8 7 L15.5 0.5" fill="none" stroke="#fff"/></svg>
    info@MarrowfieldContracting.com
  </p>

  <ul class="contact-list">
    <li><svg width="10" height="16" viewBox="0 0 10 16" aria-hidden="true"><rect x="1" y="1" width="8" height="14" rx="1.5" fill="none" stroke="var(--brand-red)" stroke-width="1.5"/></svg>(+012) 555 -0148</li>
    <li><svg width="12" height="14" viewBox="0 0 12 14" aria-hidden="true"><path d="M3 1 L5 4 L3.5 5.5 C4.5 8 6 9.5 8 10.5 L9.5 9 L12 11 L10 13.5 C5 12.5 1 8 0.5 3 Z" fill="var(--brand-red)"/></svg>(+012) 555 -0193</li>
    <li><svg width="13" height="13" viewBox="0 0 14 14" aria-hidden="true"><circle cx="7" cy="7" r="6.5" fill="var(--brand-red)"/><path d="M1 7 H13 M7 1 C4 4 4 10 7 13 M7 1 C10 4 10 10 7 13" stroke="#fff" fill="none" stroke-width="1"/></svg>www.marrowfieldcontracting.com</li>
  </ul>

  <span class="divider"></span>

  <p class="address">
    <svg width="12" height="16" viewBox="0 0 12 16" aria-hidden="true"><path d="M6 0 C2.7 0 0 2.6 0 5.8 C0 10 6 16 6 16 C6 16 12 10 12 5.8 C12 2.6 9.3 0 6 0 Z" fill="var(--brand-red)"/><circle cx="6" cy="5.8" r="2.2" fill="#fff"/></svg>
    <span><span class="address__company">Marrowfield Contracting</span> 123,<br>Lorem ipsum,678 dolor<br>sit amet</span>
  </p>
</section>

<section class="card card--back" aria-label="Business card back">
  <span class="mark-decoration" role="img" aria-label="Large brand mark decoration"></span>

  <div class="brand-name back-brand">
    <span class="brand-name__dot"></span>
    <span>Marrowfield<br>Contracting LLC</span>
  </div>
  <span class="rule rule--top"></span>

  <h2 class="services-title">Markets and Services</h2>
  <span class="rule rule--mid"></span>
  <span class="rule-dot"></span>

  <ul class="services-list">
    <li><svg width="12" height="12" viewBox="0 0 12 12" aria-hidden="true"><circle cx="6" cy="6" r="5.3" fill="none" stroke="#fff" stroke-width="1.2"/><path d="M3.3 6.2 L5.2 8 L8.7 4.2" fill="none" stroke="#fff" stroke-width="1.4"/></svg>Quis autem vel eum iure</li>
    <li><svg width="12" height="12" viewBox="0 0 12 12" aria-hidden="true"><circle cx="6" cy="6" r="5.3" fill="none" stroke="#fff" stroke-width="1.2"/><path d="M3.3 6.2 L5.2 8 L8.7 4.2" fill="none" stroke="#fff" stroke-width="1.4"/></svg>Eprehenderit qui in ea volup</li>
    <li><svg width="12" height="12" viewBox="0 0 12 12" aria-hidden="true"><circle cx="6" cy="6" r="5.3" fill="none" stroke="#fff" stroke-width="1.2"/><path d="M3.3 6.2 L5.2 8 L8.7 4.2" fill="none" stroke="#fff" stroke-width="1.4"/></svg>Tate velit esse quam nihil</li>
    <li><svg width="12" height="12" viewBox="0 0 12 12" aria-hidden="true"><circle cx="6" cy="6" r="5.3" fill="none" stroke="#fff" stroke-width="1.2"/><path d="M3.3 6.2 L5.2 8 L8.7 4.2" fill="none" stroke="#fff" stroke-width="1.4"/></svg>Molestiae consequatu</li>
  </ul>

  <p class="back-web">
    <svg width="13" height="13" viewBox="0 0 14 14" aria-hidden="true"><circle cx="7" cy="7" r="6.5" fill="#fff"/><path d="M1 7 H13 M7 1 C4 4 4 10 7 13 M7 1 C10 4 10 10 7 13" stroke="var(--brand-red)" fill="none" stroke-width="1"/></svg>
    www.marrowfieldcontracting.com
  </p>
</section>

</body>
</html>
```